Kerno Solutions: searching for a flyer to trow in letterboxes for properties we are interested in

Hello ,

Introduction:
We are a company based in Luxembourg called "Kerno Solutions". We are specialized in buying properties on which we develop and build constructions before selling them.

Informations for the flyer:
We need a flyer to trow into the letter boxes of property owners letting them know that we are interested in buying their property, if they are interested they can give us a call.

The text for the flyer/letter is in the attachment called >>2020-03-11_KS_Text for flyer,letter there might be slight changes<<.

We need to look competent, professional and financially stable.

The flyer needs to be short and not over welling with information otherwise it will land in the trash.

We have decided that we don't want real pictures on the flyer, but shapes of any kind, blue prints, drawings are fine.

Format should be in DIN A4. We plan to print the flyer on both sides in two different languages, in other words the design will be the same on both sides only the text will be in a different language.

I also added our current logo and here is the design of the website that is under construction at the moment http://www.kernosolutions-example.lu/. The logo's color can be changed into a different blue or uni color (all white or all black).
Updates

Hi, First time user the howl thing started faster as expected. Furthermore, I need to catch my boss to discust the project with him and he is on a lot of meetings. Please give us a little bit more time. Thanks

Target Market(s)

Property owners

Requirements
Must have
• email, phone number, tax number (RCS), Tax number , matriculation and address.
see word file in attachment for information
Nice to have
• Our company logo, in one form or an other, you can be creative, the logo is in the attachment.
Should not have
• Real pictures

```html
<!DOCTYPE html>
<html lang="en">
<head>
<meta charset="utf-8">
<title>Kerno Solutions – Property Flyer</title>
<link href="https://fonts.googleapis.com/css2?family=Staatliches&family=Oswald:wght@400;500&family=Open+Sans:wght@400;600&display=swap" rel="stylesheet">
<style>
  :root {
    --page-bg: #e3e4e5;
    --paper: #f0f0ef;
    --navy: #1c4a6b;
    --red: #e0403a;
    --white: #ffffff;
    --grass: #5c8a3a;
  }
  * { box-sizing: border-box; margin: 0; padding: 0; }
  html, body {
    width: 1200px; height: 800px; overflow: hidden;
    background: var(--page-bg);
  }
  .canvas {
    width: 1200px; height: 800px;
    display: flex; align-items: center; justify-content: center;
  }
  .flyer {
    position: relative;
    width: 530px; height: 750px;
    background: var(--paper);
    overflow: hidden;
  }
  .headline {
    position: absolute; left: 52px; top: 56px;
    font-family: "Staatliches", sans-serif;
    color: var(--navy);
    letter-spacing: 3px;
    line-height: 1.12;
    text-shadow: 2px 2px 0 rgba(28, 74, 107, 0.18);
  }
  .headline .line { display: block; font-size: 40px; }
  .headline .line--key { font-size: 66px; line-height: 1.05; margin: 4px 0; }
  .headline .line--accent { font-size: 66px; color: var(--red); text-shadow: 2px 2px 0 rgba(224, 64, 58, 0.2); margin-top: 4px; }

  .brand {
    position: absolute; right: 48px; top: 405px;
    display: flex; align-items: center; gap: 6px;
    font-family: "Oswald", sans-serif; font-weight: 500;
    font-size: 13px; color: var(--navy); letter-spacing: 0.5px;
  }
  .brand__mark { width: 12px; height: 12px; background: var(--navy); }

  .house-photo {
    position: absolute; left: 0; top: 460px;
    width: 215px; height: 215px;
    background: linear-gradient(160deg, #b8ad98 0%, #8f8570 45%, #5d6a45 80%, #3f5a2c 100%);
  }
  .grass-line {
    position: absolute; left: 150px; right: 0; top: 668px; height: 7px;
    background: linear-gradient(90deg, var(--grass) 0%, rgba(92, 138, 58, 0.25) 60%, rgba(92, 138, 58, 0) 100%);
  }

  .call-to-action {
    position: absolute; right: 38px; top: 500px;
    text-align: right;
    font-family: "Oswald", sans-serif; font-weight: 400;
  }
  .call-to-action__question { color: var(--navy); font-size: 18px; letter-spacing: -0.2px; }
  .call-to-action__offer { color: var(--red); font-size: 17px; line-height: 1.6; margin-top: 12px; letter-spacing: -0.2px; }
  .call-to-action__phone {
    display: flex; align-items: center; justify-content: flex-end; gap: 12px;
    margin-top: 10px;
    font-family: "Staatliches", sans-serif; font-size: 36px;
    color: var(--red); letter-spacing: 2.5px;
  }
  .call-to-action__phone svg { width: 24px; height: 28px; }

  .footer {
    position: absolute; left: 0; right: 0; bottom: 0; height: 75px;
    background: var(--navy);
    display: flex; align-items: center;
    padding-left: 34px;
    font-family: "Open Sans", sans-serif; color: var(--white);
  }
  .footer__item { font-size: 10.5px; line-height: 1.35; }
  .footer__company { font-size: 12.5px; font-weight: 600; width: 128px; }
  .footer__divider { width: 1px; height: 38px; background: rgba(255,255,255,0.75); margin: 0 14px 0 0; }
  .footer__address { width: 158px; }
</style>
</head>
<body>
<main class="canvas">
  <article class="flyer">
    <h1 class="headline">
      <span class="line">Every</span>
      <span class="line">Accomplishment</span>
      <span class="line">Starts with the</span>
      <span class="line line--key">Decision</span>
      <span class="line">To</span>
      <span class="line line--accent">Try.</span>
    </h1>

    <div class="brand">
      <span class="brand__mark"></span>
      <span class="brand__name">KERNO SOLUTIONS</span>
    </div>

    <div class="house-photo" role="img" aria-label="Photo of a two-storey family house with a porch and red windows"></div>
    <div class="grass-line"></div>

    <section class="call-to-action">
      <p class="call-to-action__question">ARE YOU PLANNING TO SELL YOUR PROPERTY?</p>
      <p class="call-to-action__offer">GIVE US A CALL WHEN YOU'LL DECIDE.<br>WE HAVE SOMETHING TO OFFER.</p>
      <p class="call-to-action__phone">
        <svg viewBox="0 0 24 28" aria-hidden="true">
          <path d="M6 2 L10 8 L7.5 10.5 C8.5 14 10.5 17 13.5 19.5 L16 17 L21 21.5 L18 25.5 C10 24 3 15 3 5 Z" fill="none" stroke="var(--navy)" stroke-width="2.2" stroke-linejoin="round"/>
        </svg>
        <span>691 000 482</span>
      </p>
    </section>

    <footer class="footer">
      <p class="footer__item footer__company">Kerno Solutions sàrl</p>
      <span class="footer__divider"></span>
      <p class="footer__item footer__address">17 rue des Vergers,<br>L-3299 Bettembourg</p>
      <span class="footer__divider"></span>
      <p class="footer__item footer__contact">info@kernosolutions-example.lu<br>www.kernosolutions-example.lu</p>
    </footer>
  </article>
</main>
</body>
</html>
```